Logo and Website Design for KM.NR Horizon - a Software Engineering and IT company

Software engineering and IT are two different disciplines - and yet inseparably linked. At KM.NR Horizon, we combine both worlds and ensure that our software solutions are not only innovative and powerful, but also integrate perfectly into existing IT landscapes. Vision stands more for imagination, so it is not neccessary something what has to do with visualisation. Please consider that the winning competitor is also instructed to make a logo for the company. So please make a suitable logo for KM.NR Horizon to which the website fits to and show it during the website creation process. A good Logo desing is important for winning the competition. The website should contain a landing page with inspiring, perhaps futuristic photos of a datacenter and lines of code. Eventuelly flewent integrated in the text. On the landing page the company should introduced with a small text (max 250 words) followed by a section with a short text to one of our products nearby a graphic visualising the architecture of the product. The menue should be on top and fixed during scrolling and consist of the menue items home, solutions, who are we and a contact button. There should be a footer for linking social media, rights and Impressum. Only as an idea not a must. The very first view on the landing page could also be the menue bar and below of it a transparent unsharp photo (e.g. datacenter, lines of code, both ;) with the company name in the center.

###############################################################

Hi Designers,

Despite your very good approaches for describing KM.NR Horizon, here a short introduction (german text) from ourself:

------
KM.NR Horizon – Ihr Partner für ganzheitliche Softwarelösungen

Die KM.NR Horizon ist ein dynamisches Unternehmen, das sich nicht nur auf die Konzeption, das Design und die Entwicklung maßgeschneiderter Software spezialisiert hat, sondern auch deren reibungslosen Betrieb sicherstellt. Mit einem Team aus erfahrenen Softwarearchitekten und IT-Professionals verbinden wir modernste Softwareentwicklung mit tiefgehendem IT-Know-how – für Lösungen, die nachhaltig, leistungsstark und zukunftssicher sind.

Software Engineering trifft IT – Perfektion in Kombination
Software Engineering und IT sind zwei unterschiedliche Disziplinen – und doch untrennbar miteinander verbunden. Wir bei KM.NR Horizon vereinen beide Welten und sorgen dafür, dass unsere Softwarelösungen nicht nur innovativ und leistungsfähig sind, sondern sich auch perfekt in bestehende IT-Landschaften integrieren.

Expertise mit Fokus auf Healthcare & komplexe IT-Umgebungen
Unsere Experten bringen jahrzehntelange Erfahrung aus dem Healthcare-Sektor mit und unterstützen IT-Abteilungen großer Kliniken in der Entwicklung und Optimierung von Softwarelösungen. Von Anwendungssoftware bis hin zu Steuerungssystemen – unsere Softwareingenieure wissen genau, worauf es ankommt.

Ganzheitlicher Ansatz – über die Software hinaus
Wir entwickeln nicht nur Software, sondern übernehmen auch die Verantwortung für deren stabile und effiziente Betriebsumgebung. Egal, ob on-premises, in der Cloud oder als SaaS-Lösung – wir kümmern uns um den kompletten Lifecycle Ihrer Anwendung.

Ihr Ziel – unser Antrieb.
Ob Neuentwicklung einer SaaS-Anwendung oder die Migration bestehender Lösungen in eine moderne SaaS-Umgebung – mit KM.NR Horizon haben Sie einen starken Partner an Ihrer Seite.

Lassen Sie uns gemeinsam die Zukunft Ihrer Software gestalten!
--------------

Our first solution called "Linked Record Transfer Gateway" (LIRTAG)
-------------------
Teilen Sie Ihre Daten sicher – ohne Kompromisse!

Sie nutzen eine relationale Datenbank (Oracle, SQL Server, Postgres etc.) und möchten ausgewählte Daten mit Dritten teilen – sei es für ein Data Warehouse, Business Controller, Lieferanten oder Kunden? Doch dabei sollen Datensicherheit, Integrität und Verfügbarkeit Ihrer primären Lösung in keiner Weise gefährdet werden?

Mit unserer Lösung erhalten Sie genau das: Maximalen Schutz für Ihre Anwendung bei gleichzeitigem Nutzen durch autorisierte Dritte – ganz ohne teure Lizenzkosten für eine Schattendatenbank.

Lassen Sie uns gemeinsam herausfinden, wie Sie Ihre Daten sicher und effizient nutzen können. Kontaktieren Sie uns – wir zeigen Ihnen, was möglich ist!
---------------------

Our second solution PLOK:
---------------------
PLOK – Program for a Tint Checking Apparatus ist die smarte Lösung für Unternehmen, die bei Farbgenauigkeit keine Kompromisse machen. Die Software erkennt Farbabweichungen zwischen Mustern vollautomatisch, beschreibt sie verständlich und sorgt so für gleichbleibend hohe Produktqualität – schnell, visuell und präzise. Perfekt für alle, die Farbe zur Vertrauenssache machen.
-------------------------

Thanks,
Matthias

Target Market(s)

IT Professionals from any sector

Industry/Entity Type

Healthcare and other

Coding

Coded - Design and coding required

Number of Pages Required

1 page

Font styles to use
Sans Serif

Colors
0054AA
0677BA
7BADD7
CADEEF
E8F1F8
0094D4
00A9DD
6FCCEA
C7EBF8
E9F6FB
00AB8E
00BBA5
67D7C9
C6EFE9
E9F9F6

Requirements
Must have
• Please see description
Nice to have
• On the landing page the company should introduced with a small text (max 250 words) followed by a section with a short text to one of our products nearby a graphic visualising the architecture of the product. The menue should be on top and fixed during scrolling and consist of the menue items home, solutions, who are we and a contact button. There should be a footer for linking social media, rights and Impressum. Only as an idea not a must. The very first view on the landing page could also be the menue bar and below of it a transparent unsharp photo (e.g. datacenter, lines of code, both ;) with the company name in the center.
Should not have
• Please see description

```html
<!DOCTYPE html>
<html lang="en">
<head>
<meta charset="utf-8">
<title>KM.NR Horizon – Software Engineering &amp; IT</title>
<link href="https://fonts.googleapis.com/css2?family=Exo+2:wght@300;400;500;600;700;800&family=Kanit:wght@300;400&family=Roboto:wght@400;500&display=swap" rel="stylesheet">
<style>
:root{
  --blue:#0054AA;
  --blue-mid:#0677BA;
  --blue-soft:#7BADD7;
  --blue-pale:#E8F1F8;
  --sky:#0094D4;
  --green:#00AB8E;
  --green-deep:#009A82;
  --ink:#0d0d0d;
  --text:#333;
  --white:#fff;
  --black:#000;
}
*{margin:0;padding:0;box-sizing:border-box}
html,body{width:1200px;height:2914px;overflow:hidden}
body{position:relative;background:var(--white);font-family:"Kanit",sans-serif;color:var(--text)}
.abs{position:absolute}
.head{font-family:"Exo 2",sans-serif}
.btn{position:absolute;display:flex;align-items:center;justify-content:center;font-family:"Exo 2",sans-serif;font-weight:700;font-size:14px;color:var(--white);border-radius:6px;background:linear-gradient(90deg,var(--green),var(--blue))}

/* hero */
.hero{left:0;top:0;width:1200px;height:560px;background:radial-gradient(ellipse at 50% 30%,#1c8fae 0%,#0a3c5c 35%,#061c33 75%,#030d1c 100%)}
.navband{left:0;top:60px;width:1200px;height:67px;background:linear-gradient(90deg,rgba(230,236,240,.92) 0%,rgba(230,236,240,.85) 30%,rgba(230,236,240,.1) 42%,rgba(230,236,240,0) 50%,rgba(230,236,240,.1) 58%,rgba(230,236,240,.85) 70%,rgba(230,236,240,.92) 100%)}
.menu-link{position:absolute;font-family:"Exo 2",sans-serif;font-weight:700;font-size:15px;text-decoration:none}
.top-nav .menu-link{top:83px;color:var(--ink)}
.top-nav .menu-link.active{color:var(--blue)}
.foot-nav .menu-link{top:2758px;color:var(--white)}
.brand{position:absolute;left:450px;width:300px;text-align:center;font-family:"Exo 2",sans-serif;font-weight:600;font-size:28px;letter-spacing:2px;color:var(--white)}
.hero-line{position:absolute;left:0;width:1200px;text-align:center;color:var(--white);font-family:"Exo 2",sans-serif}
.hero-line.l1{top:280px;font-weight:300;font-size:52px;letter-spacing:1px}
.hero-line.l2{top:342px;font-weight:800;font-size:53px}

/* about */
.about-h{left:660px;top:684px;font-size:36px;font-weight:700;color:var(--ink)}
.about-h span,.why-h span{color:var(--blue);font-weight:400}
.rule{position:absolute;height:3px;background:var(--green)}
.about-sub{left:658px;top:753px;font-size:22px;font-weight:500;color:var(--ink)}
.para{font-size:14.5px;line-height:23.2px;font-weight:300;color:#333}
.vision{left:658px;top:928px;font-family:"Exo 2",sans-serif;font-weight:600;font-size:16px;color:var(--ink);display:flex;align-items:center;gap:9px}

/* split */
.split-l{left:0;top:1218px;width:611px;height:485px;background:linear-gradient(160deg,#0a56a8,#0b5fb5 60%,#1a6fc4)}
.split-r{left:613px;top:1218px;width:587px;height:485px;background:linear-gradient(160deg,#03a087,#00957e 60%,#0aa38c)}
.split-h{color:var(--white);font-size:36px;line-height:45px}
.split-h b{font-weight:800}
.split-p{color:var(--white);font-size:15px;line-height:23px;font-weight:300}

/* why */
.why{left:0;top:1703px;width:1200px;height:543px;background:linear-gradient(180deg,#e4edf6,#eef4fa)}
.why-h{left:0;width:1200px;top:1778px;text-align:center;font-size:37px;font-weight:700;color:var(--ink)}
.card{position:absolute;width:320px;height:104px;background:var(--white);border-radius:52px;box-shadow:0 4px 18px rgba(0,60,130,.08)}
.card h4{position:absolute;top:14px;font-family:"Roboto",sans-serif;font-weight:500;font-size:15px;color:var(--ink)}
.card p{position:absolute;top:50px;font-family:"Roboto",sans-serif;font-size:13.5px;line-height:23px;color:#777;width:215px}
.card.left h4,.card.left p{right:92px;text-align:right}
.card.right h4,.card.right p{left:93px}

/* cta */
.cta-1{left:0;width:1200px;top:2350px;text-align:center;font-size:38px;font-weight:300;color:var(--blue)}
.cta-2{left:0;width:1200px;top:2406px;text-align:center;font-size:38px;font-weight:800;color:var(--ink)}

/* footer */
.footer{left:0;top:2665px;width:1200px;height:249px;background:var(--black)}
.copy{left:0;width:1200px;top:2866px;text-align:center;font-size:12.5px;color:var(--white)}
</style>
</head>
<body>

<!-- hero -->
<div class="abs hero" role="img" aria-label="Blurred data centre corridor framed by columns of glowing binary code"></div>
<div class="abs navband"></div>
<nav class="top-nav">
  <a class="menu-link active" style="left:110px">HOME</a>
  <a class="menu-link" style="left:185px">SOLUTIONS</a>
  <a class="menu-link" style="left:298px">ABOUT US</a>
  <a class="menu-link" style="left:805px">SERVICES</a>
  <a class="menu-link" style="left:904px">PRODUCT</a>
  <a class="menu-link" style="left:1000px">CONTACT</a>
</nav>
<div class="brand" style="top:74px">KM.NR Horizon</div>
<div class="hero-line l1">BRIDGING SOFTWARE &amp;</div>
<div class="hero-line l2">IT FOR A SMARTER FUTURE</div>
<div class="btn" style="left:472px;top:437px;width:255px;height:46px;border:1.5px solid rgba(255,255,255,.7);font-size:13px">DISCOVER INNOVATION TODAY</div>

<!-- about -->
<svg class="abs" style="left:100px;top:635px" width="510" height="495" role="img" aria-label="Photo of an evening city skyline connected by network lines">
  <defs><linearGradient id="photoGrad" x1="0" y1="0" x2="0" y2="1">
    <stop offset="0" stop-color="#6f9ac0"/><stop offset=".5" stop-color="#2f5680"/><stop offset="1" stop-color="#142a48"/></linearGradient></defs>
  <polygon points="120,35 390,35 480,245 390,455 120,455 30,245" fill="url(#photoGrad)" stroke="url(#photoGrad)" stroke-width="56" stroke-linejoin="round"/>
</svg>
<div class="abs about-h head">ABOUT <span>US</span></div>
<div class="rule" style="left:660px;top:734px;width:75px"></div>
<div class="abs about-sub head">Innovating Software. Engineering IT.</div>
<p class="abs para" style="left:658px;top:795px;width:440px">At KM.NR Horizon, we merge the worlds of software engineering and IT infrastructure to create powerful, scalable, and seamlessly integrated solutions. Our expertise ensures that your software is not just innovative but also works flawlessly within complex IT ecosystems.</p>
<div class="abs vision"><svg width="17" height="12" viewBox="0 0 17 12"><path d="M1 6C3.5 2 6 1 8.5 1S13.5 2 16 6C13.5 10 11 11 8.5 11S3.5 10 1 6Z" fill="none" stroke="#111" stroke-width="1.6"/><circle cx="8.5" cy="6" r="2.6" fill="#111"/></svg>VISION</div>
<p class="abs para" style="left:658px;top:957px;width:440px">We believe that software should not just be powerful—it should be perfectly aligned with IT systems.</p>
<div class="btn" style="left:658px;top:1021px;width:128px;height:44px">VIEW MORE</div>

<!-- split -->
<div class="abs split-l" role="img" aria-label="Blue tinted digital city grid"></div>
<div class="abs split-r" role="img" aria-label="Green tinted glowing network landscape"></div>
<div class="abs split-h head" style="left:111px;top:1292px"><span style="font-weight:300">THE INTEGRATION</span><br><b>ENGINE</b></div>
<div class="rule" style="left:111px;top:1388px;width:75px"></div>
<p class="abs split-p" style="left:111px;top:1413px;width:330px">A modular middleware solution that bridges legacy and modern systems, enabling seamless communication across cloud platforms, APIs, and on-premises infrastructures.</p>
<div class="btn" style="left:111px;top:1540px;width:129px;height:46px;background:var(--green);border:1.5px solid rgba(255,255,255,.8)">VIEW MORE</div>
<div class="abs split-h head" style="right:113px;top:1292px;text-align:right"><span style="font-weight:300">YOUR IT UNIVERSE</span><br><b>ALIGNED</b></div>
<div class="rule" style="left:1013px;top:1388px;width:74px;background:var(--blue)"></div>
<p class="abs split-p" style="right:113px;top:1413px;width:330px;text-align:right">A centralized control tower that gives IT teams full visibility and governance across distributed applications, services, and infrastructure components.</p>
<div class="btn" style="left:958px;top:1540px;width:129px;height:46px;background:var(--blue);border:1.5px solid rgba(255,255,255,.8)">VIEW MORE</div>
<svg class="abs" style="left:520px;top:1346px" width="176" height="168">
  <polygon points="50,14 126,14 160,84 126,154 50,154 16,84" fill="#fff" stroke="#fff" stroke-width="26" stroke-linejoin="round"/>
  <text x="88" y="90" text-anchor="middle" font-family="Exo 2,sans-serif" font-weight="600" font-size="17" fill="#0054AA">KM.NR</text>
</svg>

<!-- why -->
<div class="abs why"></div>
<div class="abs why-h head">WHY OUR APPROACH <span>STANDS OUT</span></div>
<div class="rule" style="left:563px;top:1827px;width:43px"></div>
<svg class="abs" style="left:0;top:1860px" width="1200" height="300">
  <defs>
    <radialGradient id="globe" cx=".5" cy=".5" r=".5"><stop offset="0" stop-color="#3b7fd0"/><stop offset=".6" stop-color="#1a3f80"/><stop offset="1" stop-color="#0f1e45"/></radialGradient>
  </defs>
  <g stroke="#1f74d6" stroke-width="1.3" fill="none">
    <polyline points="411,60 435,60 511,102"/><polyline points="411,224 435,224 511,182"/>
    <polyline points="737,60 713,60 637,102"/><polyline points="737,224 713,224 637,182"/>
  </g>
  <circle cx="575" cy="147" r="122" fill="#fff" stroke="#5b9ae0" stroke-width="1.2"/>
  <circle cx="575" cy="147" r="100" fill="url(#globe)" role="img" aria-label="Glowing globe with AI chip"/>
  <circle cx="575" cy="147" r="75" fill="none" stroke="#fff" stroke-width="2"/>
  <g fill="#1a7be0" stroke="#fff" stroke-width="2">
    <circle cx="411" cy="60" r="6"/><circle cx="411" cy="224" r="6"/><circle cx="737" cy="60" r="6"/><circle cx="737" cy="224" r="6"/>
    <circle cx="511" cy="102" r="6"/><circle cx="637" cy="102" r="6"/><circle cx="511" cy="182" r="6"/><circle cx="637" cy="182" r="6"/>
  </g>
</svg>
<div class="card left" style="left:90px;top:1868px"><h4>READY FOR THE WORLD</h4><p>Lorem ipsum dolor sit amet, consectetur adipiscing elit, sed do</p></div>
<div class="card left" style="left:90px;top:2033px"><h4>TRANSPARENCY LAYER</h4><p>Lorem ipsum dolor sit amet, consectetur adipiscing elit, sed</p></div>
<div class="card right" style="left:738px;top:1868px"><h4>DUAL EXPERTISE BUILT-IN</h4><p>Lorem ipsum dolor sit amet, consectetur adipiscing elit, sed do</p></div>
<div class="card right" style="left:738px;top:2033px"><h4>MODULAR ARCHITECTURE</h4><p>Lorem ipsum dolor sit amet, consectetur adipiscing elit, sed</p></div>
<svg class="abs" style="left:0;top:1860px" width="1200" height="300">
  <defs><linearGradient id="ico" x1="0" y1="0" x2="1" y2="1"><stop offset="0" stop-color="#2a8ff0"/><stop offset="1" stop-color="#0d4fc2"/></linearGradient></defs>
  <g fill="url(#ico)" stroke="#fff" stroke-width="4">
    <circle cx="362" cy="60" r="38"/><circle cx="362" cy="224" r="38"/><circle cx="785" cy="60" r="38"/><circle cx="785" cy="224" r="38"/>
  </g>
  <g fill="none" stroke="#fff" stroke-width="2" stroke-linecap="round" stroke-linejoin="round">
    <circle cx="362" cy="60" r="17"/><polyline points="354,60 360,66 371,54"/>
    <circle cx="785" cy="57" r="16"/><polyline points="778,57 783,62 792,52"/><polyline points="777,70 773,82 785,76 797,82 793,70"/>
    <circle cx="362" cy="224" r="17"/><polyline points="362,212 362,224 369,230"/>
    <circle cx="785" cy="224" r="16"/><circle cx="785" cy="224" r="6"/>
  </g>
</svg>

<!-- cta -->
<div class="abs cta-1 head">LET'S SHAPE</div>
<div class="abs cta-2 head">THE FUTURE OF IT &nbsp;- TOGETHER</div>
<div class="rule" style="left:562px;top:2456px;width:76px"></div>
<p class="abs para" style="left:250px;top:2469px;width:700px;text-align:center;font-size:15px">Whether you have a question, need a custom software solution, or want to explore how KM.NR Horizon can integrate seamlessly into your infrastructure — we're just a message away.</p>
<div class="btn" style="left:518px;top:2543px;width:166px;height:45px">GET IN TOUCH</div>

<!-- footer -->
<footer class="abs footer"></footer>
<nav class="foot-nav">
  <a class="menu-link" style="left:110px">HOME</a>
  <a class="menu-link" style="left:185px">SOLUTIONS</a>
  <a class="menu-link" style="left:298px">ABOUT US</a>
  <a class="menu-link" style="left:805px">SERVICES</a>
  <a class="menu-link" style="left:904px">PRODUCT</a>
  <a class="menu-link" style="left:1000px">CONTACT</a>
</nav>
<div class="brand" style="top:2749px">KM.NR Horizon</div>
<div class="abs copy">Copyright@2025. All Rights Reserved By KM.NR HORIZON | Privacy policy</div>
</body>
</html>
```